High End Business Card Design for Flooring Store

Looking for a new card design for our hardwood flooring company. We have no print budget for these and are open to cards made from wood, metal, cardstock with embossed print ... or any combination of these. No plastic.

We sell luxury products and I want the cards to reflect our image of quality and class.

Our contact information as such;
Employee Name
418 Colbrook Blvd.
Belmoor, NB
K9R-3M5
(555) 214-3968
Employee email @velkaflooring.com

Target Market(s)

Home Builders

Contact Information for Business Card

Emnployee name, business contact information

```html
<!DOCTYPE html>
<html lang="en">
<head>
<meta charset="utf-8">
<title>Velka Flooring – Business Card</title>
<link rel="stylesheet" href="https://fonts.googleapis.com/css2?family=Montserrat:wght@500;600&family=Open+Sans:wght@700&family=Poppins:wght@400&display=swap">
<style>
  :root {
    --page-bg: #ebe8e3;
    --card-white: #ffffff;
    --cream-band: #fbf6ef;
    --brand-red: #962a22;
    --brand-gold: #e6b228;
    --text-grey: #555555;
    --rule-gold: #e8b43a;
    --back-top: #e7b229;
    --back-mid: #c07430;
    --back-bottom: #962a23;
  }
  * { box-sizing: border-box; margin: 0; padding: 0; }
  html, body {
    width: 1189px; height: 1200px; overflow: hidden;
    background: var(--page-bg);
  }
  .canvas { position: relative; width: 1189px; height: 1200px; }

  .card {
    position: absolute; left: 169px; width: 851px; height: 485px;
    border-radius: 36px; overflow: hidden;
    box-shadow: 0 6px 18px rgba(0,0,0,0.18);
  }
  .card-front { top: 112px; background: var(--card-white); }
  .card-back {
    top: 641px;
    background: linear-gradient(180deg, var(--back-top) 0%, var(--back-mid) 52%, var(--back-bottom) 100%);
  }
  .card-bands { position: absolute; inset: 0; width: 100%; height: 100%; }
  .front-edge {
    position: absolute; left: 0; right: 0; bottom: 0; height: 9px;
    background: var(--brand-red);
  }

  .brand { position: absolute; display: flex; flex-direction: column; align-items: center; }
  .brand-row { display: flex; align-items: center; gap: 14px; }
  .brand-mark { width: 34px; height: 34px; }
  .brand-name {
    font-family: "Montserrat", sans-serif; font-weight: 500;
    font-size: 92px; line-height: 1; letter-spacing: -1px;
  }
  .brand-tagline {
    font-family: "Montserrat", sans-serif; font-weight: 500;
    font-size: 23px; line-height: 25px; text-align: center; margin-top: -6px;
  }

  .card-front .brand { left: 55px; top: 70px; width: 402px; align-items: flex-start; }
  .card-front .brand-tagline { align-self: stretch; }
  .card-front .brand-mark { background: var(--brand-gold); }
  .card-front .brand-name { color: var(--brand-red); }
  .card-front .brand-tagline { color: var(--text-grey); }

  .card-back .brand { left: 0; right: 0; top: 170px; }
  .card-back .brand-mark { background: #ffffff; }
  .card-back .brand-name, .card-back .brand-tagline { color: #ffffff; }

  .employee-name {
    position: absolute; left: 52px; top: 292px;
    font-family: "Open Sans", sans-serif; font-weight: 700;
    font-size: 29px; color: var(--brand-red); letter-spacing: -0.3px;
  }
  .name-rule {
    position: absolute; left: 55px; width: 743px; top: 345px;
    height: 2px; background: var(--rule-gold);
  }
  .contact-list {
    position: absolute; left: 52px; top: 383px;
    font-family: "Poppins", sans-serif; font-size: 22px; color: var(--text-grey);
    list-style: none;
  }
  .contact-list li { display: flex; align-items: center; height: 29px; }
  .contact-icon { width: 20px; height: 20px; margin-right: 8px; }
  .address {
    position: absolute; left: 599px; top: 362px;
    font-family: "Poppins", sans-serif; font-style: normal;
    font-size: 21px; line-height: 25.5px; color: var(--text-grey);
  }
</style>
</head>
<body>
<main class="canvas">

  <section class="card card-front" aria-label="Business card front">
    <svg class="card-bands" viewBox="0 0 851 485" aria-hidden="true">
      <polygon points="608,10 746,10 851,100 851,250" fill="var(--cream-band)"/>
      <polygon points="680,20 851,20 851,160" fill="var(--cream-band)" opacity="0.7"/>
      <polygon points="520,250 573,200 851,420 851,485 760,485" fill="var(--cream-band)"/>
    </svg>

    <div class="brand">
      <div class="brand-row">
        <span class="brand-mark"></span>
        <span class="brand-name">Velka</span>
      </div>
      <p class="brand-tagline">Planchers &amp; Escaliers<br>Flooring &amp; Stairs</p>
    </div>

    <h1 class="employee-name">EMPLOYEE NAME</h1>
    <div class="name-rule"></div>

    <ul class="contact-list">
      <li>
        <svg class="contact-icon" viewBox="0 0 20 20" aria-hidden="true">
          <path d="M5 2 L8 2 L9 6 L7 7.5 Q8.5 11.5 12 13.5 L13.5 11.5 L17 12.5 L17 15.5 Q16 17.5 13.5 17 Q4 14 3 4.5 Q3 2.5 5 2 Z" fill="var(--brand-gold)"/>
        </svg>
        (555) 214-3968
      </li>
      <li>
        <svg class="contact-icon" viewBox="0 0 20 20" aria-hidden="true">
          <rect x="1" y="4" width="18" height="12" fill="var(--brand-gold)"/>
          <path d="M1 4 L10 11 L19 4" fill="none" stroke="#fff" stroke-width="1.4"/>
        </svg>
        Employee email @velkaflooring.com
      </li>
    </ul>

    <address class="address">418 Colbrook Blvd.<br>Belmoor, NB<br>K9R-3M5</address>

    <div class="front-edge"></div>
  </section>

  <section class="card card-back" aria-label="Business card back">
    <svg class="card-bands" viewBox="0 0 851 485" aria-hidden="true">
      <polygon points="560,60 851,300 851,360 500,80" fill="#ffffff" opacity="0.05"/>
      <polygon points="640,0 760,0 851,80 851,240" fill="#ffffff" opacity="0.04"/>
      <polygon points="520,250 851,485 760,485 480,290" fill="#ffffff" opacity="0.05"/>
    </svg>

    <div class="brand">
      <div class="brand-row">
        <span class="brand-mark"></span>
        <span class="brand-name">Velka</span>
      </div>
      <p class="brand-tagline">Planchers &amp; Escaliers<br>Flooring &amp; Stairs</p>
    </div>
  </section>

</main>
</body>
</html>
```